Business card and company logo design needed

Need a business card and company logo design for all stationary for an Aviation refueling consultancy business. Our business offers consulting services in the specialist aviation refueling industry. Services range from engineering, compliance and management consultancy through to project management services. This encompasses infrastructure from refinery through to airport and into the aircraft wing.

Design should be simple, 'less-is-more' concept, possibly taking advantage of the 'm' for tovel and the fact is it the aviation industry. It should convey confidence, safety, experience, professionalism, aviation, engineering?, and should not be afraid to be simple in color...though please do not let this restrict your designs and imagination.

Target Market(s)

Airport authorities, oil majors, aircraft operators

Industry/Entity Type

Airport

Contact Information for Business Card

Verlin Skyward Advisory Pty Ltd
Dario Tovel
Director
mobile:+61428537104
email: dario@tovelexample.com
Skype: dario.tovelexample

Logo styles of interest
Emblem Logo
Pictorial/Combination Logo
Abstract Logo
Wordmark Logo
Lettermark Logo
Requirements
Must have
• - A feel of safety, security and confidence
Nice to have
• - Aviation has both heritage and modern 'sexy' elements so would be nice to try and capture both
- Aviation 'JET' fuel color is designated as black in signage or labels
- Themes? : Aviation fuel is derived from oil, it burns, safety, Jet fuel is colorless
- Company is global in reach, borderless like aircraft
Should not have
• - Cliche:

```html
<!DOCTYPE html>
<html lang="en">
<head>
<meta charset="utf-8">
<title>Verlin Skyward Advisory – Business Card</title>
<link href="https://fonts.googleapis.com/css2?family=Lato:wght@400;700&display=swap" rel="stylesheet">
<style>
  :root {
    --page-bg: #d8d4ce;
    --card-edge: #000000;
    --card-glow: #4d4d4f;
    --ink: #ffffff;
    --ink-soft: #e6e6e6;
    --shadow: rgba(0, 0, 0, 0.45);
  }
  * { box-sizing: border-box; margin: 0; padding: 0; }
  html, body {
    width: 1200px;
    height: 1000px;
    overflow: hidden;
    background: var(--page-bg);
    font-family: "Lato", Arial, sans-serif;
    color: var(--ink);
  }
  .stage {
    position: relative;
    width: 1200px;
    height: 1000px;
  }
  .card {
    position: absolute;
    top: 350px;
    width: 535px;
    height: 300px;
    background: radial-gradient(ellipse 55% 50% at 55% 45%, var(--card-glow) 0%, #2a2a2b 45%, var(--card-edge) 100%);
    box-shadow: 4px 6px 10px var(--shadow);
  }
  .card--front { left: 47px; }
  .card--back { left: 618px; }

  .brand {
    display: flex;
    align-items: center;
  }
  .brand__square {
    flex: none;
    background: var(--ink);
  }
  .brand__name {
    font-weight: 700;
    line-height: 1.25;
    color: var(--ink);
  }
  .card--front .brand {
    position: absolute;
    left: 25px;
    top: 26px;
  }
  .card--front .brand__square {
    width: 44px;
    height: 44px;
    margin-right: 14px;
  }
  .card--front .brand__name { font-size: 15px; }

  .card--back .brand {
    position: absolute;
    left: 115px;
    top: 114px;
  }
  .card--back .brand__square {
    width: 72px;
    height: 72px;
    margin-right: 22px;
  }
  .card--back .brand__name {
    font-size: 23px;
    line-height: 1.28;
  }

  .contact {
    position: absolute;
    left: 26px;
    bottom: 30px;
    list-style: none;
  }
  .contact__item {
    display: flex;
    align-items: center;
    font-size: 15px;
    color: var(--ink-soft);
    height: 24.5px;
  }
  .contact__icon {
    width: 17px;
    height: 17px;
    margin-right: 6px;
    flex: none;
  }
  .holder {
    position: absolute;
    right: 36px;
    bottom: 30px;
    text-align: center;
  }
  .holder__name {
    font-size: 20px;
    font-weight: 700;
  }
  .holder__role {
    font-size: 16px;
    margin-top: 2px;
    color: var(--ink-soft);
  }
</style>
</head>
<body>
<main class="stage">

  <section class="card card--front" aria-label="Business card front">
    <div class="brand">
      <span class="brand__square"></span>
      <p class="brand__name">Verlin Skyward<br>Advisory Pty Ltd</p>
    </div>

    <ul class="contact">
      <li class="contact__item">
        <svg class="contact__icon" viewBox="0 0 17 17" aria-hidden="true">
          <circle cx="8.5" cy="8.5" r="7.5" fill="none" stroke="#fff" stroke-width="1.4"/>
          <rect x="6" y="3.8" width="5" height="9.4" rx="1" fill="none" stroke="#fff" stroke-width="1.2"/>
          <rect x="6.9" y="5" width="3.2" height="3.2" fill="#fff"/>
        </svg>
        +61428537104
      </li>
      <li class="contact__item">
        <svg class="contact__icon" viewBox="0 0 17 17" aria-hidden="true">
          <circle cx="8.5" cy="8.5" r="7.5" fill="none" stroke="#fff" stroke-width="1.4"/>
          <circle cx="8.5" cy="8.5" r="2.4" fill="none" stroke="#fff" stroke-width="1.3"/>
          <path d="M10.9 6.4v3.2c0 1.2 1.9 1.2 1.9-0.4 0-2.6-1.9-4.4-4.3-4.4" fill="none" stroke="#fff" stroke-width="1.3"/>
        </svg>
        dario@tovelexample.com
      </li>
      <li class="contact__item">
        <svg class="contact__icon" viewBox="0 0 17 17" aria-hidden="true">
          <circle cx="8.5" cy="8.5" r="7.5" fill="none" stroke="#fff" stroke-width="1.4"/>
        </svg>
        dario.tovelexample
      </li>
    </ul>

    <div class="holder">
      <p class="holder__name">Dario Tovel</p>
      <p class="holder__role">Director</p>
    </div>
  </section>

  <section class="card card--back" aria-label="Business card back">
    <div class="brand">
      <span class="brand__square"></span>
      <p class="brand__name">Verlin Skyward<br>Advisory Pty Ltd</p>
    </div>
  </section>

</main>
</body>
</html>
```